Redesign website bus travel company Lenz Tavan

We require a complete redesign of the website of Reisebüro Lenz Tavan, an established bus tour operator based in Graubünden (www.lenztavan-beispiel.ch). For years, the company has specialized in multi-day tours throughout Europe, as well as day trips such as shopping trips to Innsbruck or Como, music tours, and market visits, primarily for seniors, as well as car rentals for clubs and companies.

The new website requires a video header with overlay text, red as the primary corporate color, complemented by black and gray, and a highly simplified navigation with two main sections: "Our Trips" and "Bus Rental." The remaining sections must be accessible via the "Menu" menu item. The design should be user-friendly for all age groups and mobile-responsive.

The goal is a trustworthy, modern website that reflects personal service and many years of experience.
The new logo can be found in the files, as well as a few pictures.

Target Market(s)

Guests of bus tours (day and multi-day trips) and bus rentals (clubs, companies, etc.)

Industry/Entity Type

Busreisen und Busvermietung

Number of Pages Required

1 page

Requirements
Must have
• Red as primary color, video header, simple UX for target group seniors
Nice to have
• Photo galleries of destinations and the vehicle fleet

```html
<!DOCTYPE html>
<html lang="de">
<head>
<meta charset="utf-8">
<title>Reisebüro Lenz Tavan</title>
<link href="https://fonts.googleapis.com/css2?family=DM+Sans:wght@400;500;600;700&family=Inter:wght@400;500;600&display=swap" rel="stylesheet">
<style>
:root{
  --red:#c8161d;
  --orange:#e8542f;
  --ink:#111214;
  --dark:#1f3b2c;
  --gray:#6b6f76;
  --muted:#8a8f96;
  --beige:#f8f6f2;
  --line:#d9d9d9;
  --star:#f5b82e;
  --link:#6a7aa8;
}
*{margin:0;padding:0;box-sizing:border-box}
html,body{width:1200px;height:2721px;overflow:hidden}
body{position:relative;background:#fff;font-family:"Inter",sans-serif;color:var(--ink)}
.abs{position:absolute}
.hero-bg{left:0;top:0;width:1200px;height:880px;background:radial-gradient(ellipse at 0% 20%,#fdf3e6 0%,rgba(255,255,255,0) 45%),radial-gradient(ellipse at 100% 35%,#f9e1e0 0%,rgba(255,255,255,0) 50%),#fff}
.brand{font-family:"DM Sans",sans-serif;font-weight:700;color:var(--red);font-size:26px;display:flex;align-items:center;gap:10px}
.brand i{display:block;width:14px;height:14px;border-radius:50%;background:var(--red)}
.nav{left:619px;top:38px;display:flex;gap:27px;font-size:13.5px;color:var(--gray)}
.nav .active{color:var(--dark);font-weight:600}
.btn{left:930px;top:24px;width:170px;height:47px;border-radius:24px;background:var(--red);color:#fff;font-weight:600;font-size:13.5px;display:flex;align-items:center;justify-content:center;gap:8px}
h1{font-family:"DM Sans",sans-serif;font-weight:700;font-size:40px;line-height:46px;letter-spacing:-1.4px;text-align:center;width:1200px;top:152px;left:0}
.sub{top:259px;left:0;width:1200px;text-align:center;font-size:13.5px;color:var(--gray)}
.tabs{top:332px;left:0;width:1200px;display:flex;justify-content:center;align-items:center;font-size:21px;color:var(--muted)}
.tabs span{padding:0 30px}
.tabs .sep{width:2px;height:24px;background:var(--ink);padding:0}
.tabs .cur{color:var(--red);font-weight:600;text-decoration:underline;text-underline-offset:6px;text-decoration-thickness:3px}
.band{left:0;top:871px;width:1200px;height:601px;background:var(--beige)}
.hero-photo{left:175px;top:403px;width:850px;height:498px;border-radius:12px;background:linear-gradient(100deg,#5d6a3c 0%,#3f4636 30%,#2b2d33 55%,#1f4f8a 80%,#3b82c9 100%);box-shadow:0 18px 40px rgba(0,0,0,.25)}
h2{font-family:"DM Sans",sans-serif;font-weight:700;letter-spacing:-1.6px}
.travel{left:100px;top:955px;font-size:50px;line-height:54px}
.travel-text{left:628px;top:999px;width:470px;font-size:13.5px;line-height:22px}
.feat{top:1136px;width:280px}
.feat h3{font-family:"DM Sans",sans-serif;font-weight:700;font-size:21px;letter-spacing:-.4px;margin:14px 0 18px}
.feat p{font-size:15px;line-height:23.3px;color:var(--gray)}
.more{font-size:12px;font-weight:500;color:var(--orange);display:flex;align-items:center;gap:8px;margin-top:22px}
.clients{left:100px;top:1563px;font-size:34px;line-height:40px;font-weight:500;letter-spacing:-.6px}
.clients-text{left:739px;top:1581px;width:380px;font-size:13.5px;line-height:22px;color:var(--gray)}
.person{left:147px;top:1736px;width:377px;height:277px;border-radius:10px;background:linear-gradient(120deg,#8c5a3a 0%,#d9d2c6 35%,#b8c8dc 65%,#6f6a62 100%)}
.quote{left:608px;top:1800px;width:420px;font-family:"DM Sans",sans-serif;font-weight:700;font-size:21px;line-height:24px}
.who{left:608px;top:1966px;font-family:"DM Sans",sans-serif;font-weight:700;font-size:15px}
.role{left:608px;top:1989px;font-size:13.5px;color:var(--gray)}
.dots{left:608px;top:2032px;display:flex;gap:11px}
.dots i{width:9px;height:9px;border-radius:50%;background:#d7dce0}
.dots i:first-child{background:var(--dark)}
.stat-h{left:147px;top:2105px;font-size:33px;line-height:40px;letter-spacing:-1.3px}
.stat-sub{left:147px;top:2192px;font-size:13.5px;color:var(--gray)}
.rate{top:2112px;font-family:"DM Sans",sans-serif}
.rate b{font-size:34px;font-weight:600;display:block;letter-spacing:-1px}
.rate .stars{color:var(--star);font-size:17px;letter-spacing:3px;margin-top:2px}
.rate small{display:block;font-family:"Inter",sans-serif;font-size:12px;color:var(--gray);margin-top:6px}
.vline{left:882px;top:2105px;width:1px;height:90px;background:var(--line)}
.foot-bg{left:0;top:2340px;width:1200px;height:381px;background:radial-gradient(ellipse at 100% 100%,#f6dcdc 0%,rgba(255,255,255,0) 60%),linear-gradient(90deg,#fdf6ee,#fbf1f0)}
.tagline{left:100px;top:2470px;font-size:15.5px}
.contact{left:100px;font-size:13.5px;display:flex;align-items:center}
.contact .lbl{width:137px;display:flex;align-items:center;gap:14px;font-weight:500}
.contact .val{font-size:12px}
.col{top:2400px}
.col h4{font-family:"DM Sans",sans-serif;font-weight:600;font-size:17px;margin-bottom:18px}
.col a{display:block;font-size:12px;color:var(--gray);text-decoration:none;line-height:27.5px}
.hr{left:100px;top:2643px;width:1000px;height:1px;background:#bfc3c8}
.legal{top:2670px;font-size:9.5px;color:var(--link);font-weight:500}
.social{left:983px;top:2668px;display:flex;gap:20px}
.social i{width:14px;height:14px;border-radius:50%;background:var(--ink)}
</style>
</head>
<body>
<div class="abs hero-bg"></div>

<div class="abs brand" style="left:87px;top:32px"><i></i>Lenz Tavan</div>
<nav class="abs nav"><span class="active">About</span><span>Our Trips</span><span>Bus Rental</span><span>Menu</span></nav>
<div class="abs btn">
  <svg width="15" height="12" viewBox="0 0 15 12" fill="none" stroke="#fff" stroke-width="1.6"><rect x="1" y="1" width="13" height="10" rx="1.5"/><path d="M1.5 2l6 4.5 6-4.5"/></svg>
  Conactact Now
</div>

<h1 class="abs">Erleben Sie unvergessliche Reisen ab<br>Chur – bequem, sicher und persönlich</h1>
<svg class="abs" style="left:915px;top:147px" width="28" height="26" viewBox="0 0 28 26" fill="none" stroke="#f5b82e" stroke-width="3" stroke-linecap="round"><path d="M4 14L12 3"/><path d="M10 20L24 12"/></svg>
<p class="abs sub">Entdecken Sie unser Tagesfahrten- und Mehr-Tagesprogramm 2025.</p>
<div class="abs tabs"><span class="cur">Our Trips</span><span class="sep"></span><span>Bus Rental</span><span class="sep"></span><span>Know More</span></div>
<svg class="abs" style="left:715px;top:360px" width="56" height="10" viewBox="0 0 56 10" fill="none" stroke="#f5b82e" stroke-width="2" stroke-linecap="round"><path d="M2 3c15 7 35 7 52 0"/></svg>

<div class="abs band"></div>
<div class="abs hero-photo" role="img" aria-label="Zwei lachende Reisegäste vor einem blauen Reisebus in der Stadt"></div>

<h2 class="abs travel">Travel<br>Comfortably</h2>
<p class="abs travel-text">Whether you’re joining a music tour, a scenic multi-day escape, or a relaxing shopping day in Como or Innsbruck — our tours are thoughtfully planned, senior-friendly, and personally hosted.</p>

<div class="abs feat" style="left:102px">
  <svg width="36" height="38" viewBox="0 0 36 38" fill="none" stroke="#e8542f" stroke-width="2.4" stroke-linejoin="round"><path d="M3 16L18 3l15 13v19H3z"/><path d="M13 35V22h10v13"/></svg>
  <h3>Ausflug &amp; Erlebnis</h3>
  <p>Genuss unterwegs: Bergseen, kulinarische Entdeckungen oder Geheimtipps wie Bannalpsee inkl. Seilbahn &amp; regionalem Mittagessen.</p>
  <div class="more">See more <svg width="16" height="12" viewBox="0 0 16 12" fill="none" stroke="#e8542f" stroke-width="1.5"><path d="M1 6h14M10 1l5 5-5 5"/></svg></div>
</div>
<div class="abs feat" style="left:442px">
  <svg width="40" height="38" viewBox="0 0 40 38" fill="none" stroke="#e8542f" stroke-width="2.4"><rect x="2" y="6" width="36" height="26" rx="3"/><path d="M2 15h36"/></svg>
  <h3>Shopping &amp; Märkte</h3>
  <p>Entdecken Sie Europas Top-Märkte &amp; Einkaufsziele. Abfahrt ab Chur, Rückkehr am Abend. Inklusive praxistauglicher Infos zu Preis, Abfahrtszeit und Ticketoptionen.</p>
  <div class="more">See more <svg width="16" height="12" viewBox="0 0 16 12" fill="none" stroke="#e8542f" stroke-width="1.5"><path d="M1 6h14M10 1l5 5-5 5"/></svg></div>
</div>
<div class="abs feat" style="left:781px">
  <svg width="38" height="38" viewBox="0 0 38 38" fill="none" stroke="#e8542f" stroke-width="2.4" stroke-linejoin="round"><path d="M3 17h7v18H3z"/><path d="M10 17l7-14c3 0 5 2 4 6l-2 7h12c2 0 4 2 3 4l-3 12c-1 2-2 3-4 3H10"/></svg>
  <h3>Musik &amp; Konzerte</h3>
  <p>Live-Erlebnisse ohne Stress – günstige Car-Fahrten zu Konzerten in Zürich und Umgebung. Einfach, verlässlich.</p>
  <div class="more">See more <svg width="16" height="12" viewBox="0 0 16 12" fill="none" stroke="#e8542f" stroke-width="1.5"><path d="M1 6h14M10 1l5 5-5 5"/></svg></div>
</div>

<h2 class="abs clients">Our happy clients<br>says about us</h2>
<p class="abs clients-text">These are the opinion of those who have travelled with us most recently.</p>

<div class="abs person" role="img" aria-label="Porträt eines zufriedenen Reisegastes im hellblauen Hemd"></div>
<svg class="abs" style="left:608px;top:1738px" width="42" height="32" viewBox="0 0 42 32" fill="#8f96a3"><path d="M2 30V18C2 8 7 3 17 1l1 4c-5 2-7 5-7 10h7v15zM24 30V18c0-10 5-15 15-17l1 4c-5 2-7 5-7 10h7v15z"/></svg>
<p class="abs quote">“Traveling with Lenz Tavan was a delight — from the first booking call to stepping off the bus in Verona. Friendly drivers, well-planned stops, and absolute comfort throughout. I’ve already booked my next trip!”</p>
<p class="abs who">— Lukas Meier</p>
<p class="abs role">Product Manager, Nordwerk</p>
<div class="abs dots"><i></i><i></i><i></i><i></i></div>

<h2 class="abs stat-h">More than 3,000 happy travelers<br>each year trust Reisebüro Lenz Tavan</h2>
<p class="abs stat-sub">Personal service. Decades of experience. European memories made easy.</p>
<div class="abs rate" style="left:753px"><b>4,9</b><div class="stars">★★★★★</div><small>Reiseportal</small></div>
<div class="abs vline"></div>
<div class="abs rate" style="left:917px"><b>5,0</b><div class="stars">★★★★★</div><small>Kundenstimmen</small></div>

<div class="abs foot-bg"></div>
<div class="abs brand" style="left:100px;top:2418px"><i></i>Lenz Tavan</div>
<p class="abs tagline">Seit 1956 – Persönlich. Komfortabel. Europaweit.</p>
<div class="abs contact" style="top:2534px"><span class="lbl"><svg width="18" height="18" viewBox="0 0 18 18" fill="none" stroke="#111" stroke-width="1.4"><path d="M9 17s6-6 6-10A6 6 0 003 7c0 4 6 10 6 10z"/><circle cx="9" cy="7" r="2"/></svg>Address</span><span class="val">Beispielweg 12, 7000 Chur, Schweiz</span></div>
<div class="abs contact" style="top:2567px"><span class="lbl"><svg width="18" height="18" viewBox="0 0 18 18" fill="none" stroke="#111" stroke-width="1.4"><rect x="1.5" y="3.5" width="15" height="11" rx="1"/><path d="M2 4l7 6 7-6"/></svg>Contact Us</span><span class="val">info@lenztavan-beispiel.ch</span></div>
<div class="abs contact" style="top:2601px"><span class="lbl"><svg width="18" height="18" viewBox="0 0 18 18" fill="none" stroke="#111" stroke-width="1.4"><path d="M4 2l3 3-2 2c1 3 3 5 6 6l2-2 3 3-2 2C8 16 2 10 2 4z"/></svg>Contact Us</span><span class="val">+41 81 000 00 00</span></div>

<div class="abs col" style="left:611px"><h4>Website</h4><a>Startseite</a><a>Unsere Reisen</a><a>Busvermietung</a><a>Über Uns</a><a>Kontakt</a></div>
<div class="abs col" style="left:819px"><h4>Highlights</h4><a>Tagesfahrten</a><a>Mehrtagesreisen</a><a>Shopping &amp; Märkte</a><a>Musik &amp; Konzerte</a><a>Gruppenreisen</a></div>

<div class="abs hr"></div>
<p class="abs legal" style="left:100px">© Reisebüro Lenz Tavan</p>
<p class="abs legal" style="left:365px">Privacy and Terms</p>
<p class="abs legal" style="left:474px">Legal</p>
<p class="abs legal" style="left:522px">AGB &amp; Datenschutz</p>
<p class="abs legal" style="left:636px">Impressum</p>
<p class="abs legal" style="left:711px">Sprachauswahl: DE | EN</p>
<div class="abs social"><i></i><i></i><i></i><i></i></div>
</body>
</html>
```